| ▼ターゲット 10〜40代女性 健康重視な方、天然成分のサプリメントで体調管理したい方 その他6商品ほどの自社商品を出し、「お悩め解決」をテーマにしてシリーズ化を検討しております。 ▼希望デザイン方針 若くてスタイリッシュなイメージ。野菜成分仕様のため、白・緑の配色が希望 デザインイメージは添付の他社イメージを参考してください。 ▼制作依頼案 今回作っていただくのはランディングページのバナー部分となります。 今回依頼させて頂いた方にその他、同じ商品の商品紹介画像・バナー、計5〜8点のデザインをプロジェクト形式で依頼いたします。 また、今後別途依頼で別商品もお願いさせて頂く可能性があります。 ▼商品名 ブロッコリースプラウト https://www.kaimonoya-shop.jp/item/K72TQW918X/ ▼商品特徴 配合成分「ブロッコリースプラウト、明日葉、金時生姜」 スッキリする、内側からの美しさを取り入れる、自然野菜成分使用。 医薬品GMP工場で製造されたのサプリメントです。 ▼選定基準 コンセプトやイメージに沿うもの 決定後何度か修正が入る可能性がありますが、対応頂ける方。 |
皆さん素敵な提案をありがとうございました!色々迷いましたが最終的にこの提案を採用させて頂きます。理由シンプルなデザインで、弊社商品のスッキリしたイメージに適しているからです。
皆様、すばらしいご提案ありがとうございました。
今回はご縁がありませんでしたが、またの機会にお願いできればと考えております。

```html
<!DOCTYPE html>
<html lang="ja">
<head>
<meta charset="UTF-8">
<title>ブロッコリースプラウト バナー</title>
<link rel="stylesheet" href="https://fonts.googleapis.com/css2?family=M+PLUS+Rounded+1c:wght@500;800&family=Noto+Sans+JP:wght@500;700;900&display=swap">
<style>
  :root {
    --green-deep: #2f8a2a;
    --green-mid: #5fae3c;
    --green-pale: #dff0c8;
    --green-mist: #eef7e4;
    --white: #ffffff;
    --red-band: #c8161d;
    --red-text: #c0271d;
    --pink: #e8589a;
    --text-dark: #333333;
    --ginger: #d9b86a;
    --tablet: #6f7f3c;
  }
  html, body {
    margin: 0;
    padding: 0;
    width: 1200px;
    height: 372px;
    overflow: hidden;
    background: var(--white);
  }
  .banner {
    position: relative;
    width: 1200px;
    height: 372px;
    overflow: hidden;
    background: linear-gradient(90deg, var(--white) 0%, var(--white) 30%, var(--green-mist) 100%);
    font-family: "Noto Sans JP", sans-serif;
  }
  .banner * { white-space: nowrap; }
  .sprout-field {
    position: absolute;
    left: 340px;
    top: 0;
    width: 860px;
    height: 372px;
    background:
      radial-gradient(ellipse at 60% 85%, #b9dc8f 0%, rgba(200,228,165,0.6) 40%, rgba(238,247,228,0) 75%),
      linear-gradient(90deg, rgba(255,255,255,0) 0%, #e3f1d2 60%, #d6ebbd 100%);
    opacity: 0.85;
  }
  .promise-badge {
    position: absolute;
    left: 10px;
    top: 50px;
    width: 220px;
    height: 220px;
    border-radius: 50%;
    background: var(--green-pale);
    display: flex;
    align-items: center;
    justify-content: center;
  }
  .promise-badge__inner {
    width: 192px;
    height: 192px;
    border-radius: 50%;
    background: var(--white);
    display: flex;
    flex-direction: column;
    align-items: center;
    justify-content: center;
    font-family: "M PLUS Rounded 1c", sans-serif;
    font-weight: 800;
    line-height: 1.3;
  }
  .promise-badge__lead { color: var(--green-deep); font-size: 28px; }
  .promise-badge__key { color: var(--red-text); font-size: 30px; }
  .cert-mark {
    position: absolute;
    left: 12px;
    top: 268px;
    width: 48px;
    height: 48px;
    border-radius: 50%;
    background: var(--white);
    border: 3px solid var(--green-mid);
    box-sizing: border-box;
  }
  .maker-band {
    position: absolute;
    left: 0;
    top: 320px;
    width: 362px;
    height: 36px;
    background: var(--red-band);
    color: var(--white);
    font-weight: 700;
    font-size: 18px;
    display: flex;
    align-items: center;
    padding-left: 12px;
    box-sizing: border-box;
  }
  .product-title {
    position: absolute;
    left: 510px;
    top: 10px;
    margin: 0;
    font-family: "M PLUS Rounded 1c", sans-serif;
    font-weight: 800;
    font-size: 44px;
    line-height: 60px;
    color: var(--green-deep);
    text-shadow: 0 0 6px var(--white), 0 0 6px var(--white);
  }
  .product-tagline {
    position: absolute;
    left: 530px;
    top: 78px;
    margin: 0;
    font-size: 16px;
    line-height: 26px;
    font-weight: 500;
    color: var(--text-dark);
    text-shadow: 0 0 4px var(--white);
  }
  .ingredient-label {
    position: absolute;
    top: 118px;
    font-size: 18px;
    font-weight: 700;
    color: var(--green-deep);
    background: var(--white);
    padding: 1px 6px;
    border-radius: 4px;
  }
  .ingredient-label--ashitaba { left: 366px; }
  .ingredient-label--ginger { left: 536px; }
  .ingredient-visual {
    position: absolute;
    border-radius: 16px;
  }
  .ingredient-visual--ashitaba {
    left: 360px; top: 152px; width: 160px; height: 150px;
    background: radial-gradient(ellipse, #a8cf6e 0%, #c9e3a0 55%, rgba(255,255,255,0) 80%);
  }
  .ingredient-visual--ginger {
    left: 520px; top: 152px; width: 170px; height: 150px;
    background: radial-gradient(ellipse at 40% 40%, var(--ginger) 0%, #eedcae 45%, #cfe6a9 70%, rgba(255,255,255,0) 85%);
  }
  .blend-mark {
    position: absolute;
    left: 514px;
    top: 298px;
    width: 62px;
    height: 62px;
    border-radius: 50%;
    background: var(--pink);
    color: var(--white);
    font-weight: 900;
    font-size: 20px;
    display: flex;
    align-items: center;
    justify-content: center;
    border: 3px solid var(--white);
  }
  .dose-info {
    position: absolute;
    left: 780px;
    top: 152px;
    width: 142px;
    font-size: 18px;
    font-weight: 500;
    color: var(--text-dark);
    line-height: 1.25;
    text-align: right;
  }
  .tablet-visual {
    position: absolute;
    left: 712px;
    top: 210px;
    width: 228px;
    height: 150px;
    border-radius: 14px;
    background: linear-gradient(160deg, #8a9a4e, var(--tablet));
  }
  .package-visual {
    position: absolute;
    left: 1012px;
    top: 10px;
    width: 170px;
    height: 350px;
    border-radius: 10px;
    background: linear-gradient(170deg, #4f9a3c 0%, #2c6f28 60%, #dfe9d4 100%);
  }
</style>
</head>
<body>
  <div class="banner">
    <div class="sprout-field" role="img" aria-label="ブロッコリースプラウトの新芽の写真"></div>

    <div class="promise-badge">
      <div class="promise-badge__inner">
        <span class="promise-badge__lead">ぎゅ〜っと</span>
        <span class="promise-badge__key">濃縮!!</span>
      </div>
    </div>

    <div class="cert-mark" aria-hidden="true"></div>
    <div class="maker-band">越中くすり舎 医薬品GMP工場製造</div>

    <h1 class="product-title">ブロッコリースプラウト</h1>
    <p class="product-tagline">スッキリ、内側からの美しさを取り入れる、自然野菜成分使用。</p>

    <div class="ingredient-visual ingredient-visual--ashitaba" role="img" aria-label="明日葉の葉の写真"></div>
    <div class="ingredient-visual ingredient-visual--ginger" role="img" aria-label="金時生姜の写真"></div>
    <span class="ingredient-label ingredient-label--ashitaba">・明日葉</span>
    <span class="ingredient-label ingredient-label--ginger">・金時生姜</span>
    <div class="blend-mark">配合</div>

    <div class="tablet-visual" role="img" aria-label="緑色の錠剤の写真"></div>
    <div class="dose-info">1ヶ月 60粒<br>30mg</div>
    <div class="package-visual" role="img" aria-label="ブロッコリースプラウトのサプリメント袋の写真"></div>
  </div>
</body>
</html>
```